Psychotherapist need a business card with logo

I am a psychotherapist in need of a business card. The card must have:

Marisol Trevuneda
Psicoterapeuta
937 281 706

Psychologists use the greek letter psy, which is the psychologist symbol, but I would prefer something like a mandala, a graphic symbol, an iconic tree, nothing very usual, but something that shows confidence and trust.

Industry/Entity Type

Business

```html
<!DOCTYPE html>
<html lang="es">
<head>
<meta charset="utf-8">
<title>Marisol Trevuneda · Psicoterapia</title>
<link href="https://fonts.googleapis.com/css2?family=Allura&family=Didact+Gothic&display=swap" rel="stylesheet">
<style>
  :root {
    --backdrop: #e9e9e9;
    --card: #f0eee9;
    --ink: #3b3734;
    --ink-soft: #4a4644;
    --rule: #6f6c69;
    --leaf-deep: #4f9a6c;
    --leaf-light: #8fc38e;
    --leaf-pale-deep: #a9c4ab;
    --leaf-pale-light: #cddccb;
  }
  * { box-sizing: border-box; margin: 0; padding: 0; }
  html, body {
    width: 1200px;
    height: 720px;
    overflow: hidden;
    background: var(--backdrop);
  }
  .canvas {
    position: relative;
    width: 1200px;
    height: 720px;
  }
  .card {
    position: absolute;
    top: 241px;
    width: 420px;
    height: 240px;
    background: var(--card);
    font-family: "Didact Gothic", sans-serif;
    color: var(--ink);
  }
  .card--front { left: 147px; }
  .card--back { left: 633px; }

  .tree-mark {
    position: absolute;
    left: 50%;
    transform: translateX(-50%);
    border-radius: 50%;
  }
  .card--front .tree-mark {
    top: 19px;
    width: 82px;
    height: 82px;
    background: radial-gradient(circle at 45% 40%, var(--leaf-light), var(--leaf-deep));
  }
  .card--back .tree-mark {
    top: 18px;
    width: 80px;
    height: 80px;
    background: radial-gradient(circle at 45% 40%, var(--leaf-pale-light), var(--leaf-pale-deep));
  }

  .holder-name {
    position: absolute;
    top: 112px;
    left: 0;
    width: 100%;
    text-align: center;
    font-family: "Allura", cursive;
    font-size: 30px;
    line-height: 36px;
    color: var(--ink);
  }
  .front-rule {
    position: absolute;
    top: 155px;
    left: 85px;
    width: 250px;
    height: 1px;
    background: var(--rule);
  }
  .front-title {
    position: absolute;
    top: 166px;
    left: 0;
    width: 100%;
    text-align: center;
    font-size: 12px;
    letter-spacing: 4px;
    padding-left: 4px;
    color: var(--ink-soft);
  }
  .front-phone {
    position: absolute;
    top: 192px;
    left: 0;
    width: 100%;
    text-align: center;
    font-size: 10.5px;
    letter-spacing: 1.5px;
    color: var(--ink);
  }

  .back-rule {
    position: absolute;
    left: 41px;
    width: 338px;
    height: 1px;
    background: var(--rule);
  }
  .back-rule--top { top: 105px; }
  .back-rule--bottom { top: 136px; }
  .back-title {
    position: absolute;
    top: 107px;
    left: 0;
    width: 100%;
    text-align: center;
    font-size: 24px;
    line-height: 28px;
    letter-spacing: 14px;
    padding-left: 14px;
    color: var(--ink-soft);
  }
</style>
</head>
<body>
  <div class="canvas">
    <section class="card card--front">
      <div class="tree-mark" role="img" aria-label="Símbolo de árbol con hojas verdes"></div>
      <p class="holder-name">Marisol Trevuneda</p>
      <div class="front-rule"></div>
      <p class="front-title">PSICOTERAPIA</p>
      <p class="front-phone">937 281 706</p>
    </section>

    <section class="card card--back">
      <div class="tree-mark" role="img" aria-label="Símbolo de árbol en verde suave"></div>
      <div class="back-rule back-rule--top"></div>
      <p class="back-title">PSICOTERAPIA</p>
      <div class="back-rule back-rule--bottom"></div>
    </section>
  </div>
</body>
</html>
```